Mobile App Screen Design for Dog Kennels App

Design a single home page design for an iphone app.

A PhotoShop file must be provided with all layers individually available so they can be modified.

The customers website
http://www.brindlewoodhoundhouse-example.com/
and Facebook account
https://www.facebook.com/Brindlewood-Hound-House-913274058216437/?fref=ts
can be used for reference.

The company name "Brindlewood Hound House" should appear on the home page other than that there is free reign on the design.

Any questions let me know.

```html
<!DOCTYPE html>
<html lang="en">
<head>
<meta charset="utf-8">
<title>Brindlewood Hound House – Home</title>
<link rel="stylesheet" href="https://fonts.googleapis.com/css2?family=Fira+Sans:wght@400;700&display=swap">
<style>
  :root {
    --page-bg: #e8e7e3;
    --cream: #fbf8ea;
    --forest: #4b6a4b;
    --lime: #8cc126;
    --status-bg: #0d0d0d;
    --status-text: #ffffff;
    --dot-muted: #a9b5a3;
    --puppy-light: #d49a5a;
    --puppy-mid: #b5733a;
    --puppy-dark: #7a4a22;
    --logo-tone: #9b6a3c;
  }
  * { box-sizing: border-box; margin: 0; padding: 0; }
  html, body {
    width: 1120px; height: 1200px; overflow: hidden;
    background: var(--page-bg);
    font-family: "Fira Sans", Arial, sans-serif;
  }
  .app-screen {
    position: absolute; left: 240px; top: 32px;
    width: 640px; height: 1136px;
    background: var(--cream);
    overflow: hidden;
  }
  .status-bar {
    position: absolute; left: 0; top: 0; width: 100%; height: 56px;
    background: var(--status-bg); color: var(--status-text);
    display: flex; align-items: center; justify-content: space-between;
    padding: 0 18px; font-size: 24px;
  }
  .status-left, .status-right { display: flex; align-items: center; gap: 10px; }
  .status-time { position: absolute; left: 0; right: 0; text-align: center; font-weight: 700; pointer-events: none; }
  .grass-field { position: absolute; left: 0; top: 0; }
  .brand-title {
    position: absolute; left: 0; top: 82px; width: 100%;
    text-align: center; color: var(--forest); font-weight: 700; line-height: 1.08;
  }
  .brand-title .line-main { display: block; font-size: 52px; }
  .brand-title .line-sub { display: block; font-size: 44px; }
  .kennel-illustration {
    position: absolute; left: 222px; top: 264px; width: 172px; height: 120px;
    border-radius: 14px;
    background: linear-gradient(135deg, var(--logo-tone), #c98f55);
  }
  .hero-ring { position: absolute; left: 54px; top: 420px; }
  .hero-photo {
    position: absolute; left: 117px; top: 483px; width: 406px; height: 406px;
    border-radius: 50%;
    background: radial-gradient(circle at 45% 40%, var(--puppy-light), var(--puppy-mid) 55%, var(--puppy-dark));
  }
  .carousel-dots {
    position: absolute; top: 1001px; left: 0; width: 100%;
    display: flex; justify-content: center; gap: 30px;
  }
  .carousel-dots span { width: 20px; height: 20px; border-radius: 50%; background: var(--dot-muted); }
  .carousel-dots span.is-active { background: var(--forest); }
  .call-button {
    position: absolute; left: 24px; top: 1063px; width: 594px; height: 62px;
    background: var(--forest); color: #ffffff; border: 0;
    font-family: "Fira Sans", Arial, sans-serif; font-size: 32px;
    display: flex; align-items: center; justify-content: center;
  }
</style>
</head>
<body>
<main class="app-screen">
  <svg class="grass-field" width="640" height="1136" viewBox="0 0 640 1136" role="img" aria-label="Green lawn illustration framing the photo">
    <path fill="var(--lime)" d="M0 352 C120 340 200 358 320 346 C440 336 540 354 640 340 L640 600 C640 648 628 680 606 702 C610 650 612 600 612 560 C610 470 520 420 330 420 C150 420 66 470 62 570 L62 700 C48 722 28 732 0 736 Z"/>
  </svg>

  <header class="status-bar">
    <div class="status-left">
      <svg width="86" height="14" viewBox="0 0 86 14" aria-hidden="true">
        <circle cx="7" cy="7" r="6" fill="#fff"/><circle cx="24" cy="7" r="6" fill="#fff"/>
        <circle cx="41" cy="7" r="6" fill="#fff"/><circle cx="58" cy="7" r="6" fill="#fff"/>
        <circle cx="75" cy="7" r="5" fill="none" stroke="#fff" stroke-width="1.5"/>
      </svg>
      <span class="status-carrier">MAPLE</span>
      <svg width="26" height="20" viewBox="0 0 26 20" aria-hidden="true">
        <path d="M2 7 A16 16 0 0 1 24 7" fill="none" stroke="#fff" stroke-width="3"/>
        <path d="M6 11 A10 10 0 0 1 20 11" fill="none" stroke="#fff" stroke-width="3"/>
        <circle cx="13" cy="16" r="3" fill="#fff"/>
      </svg>
    </div>
    <span class="status-time">4:21 PM</span>
    <div class="status-right">
      <span class="status-battery-level">22%</span>
      <svg width="48" height="22" viewBox="0 0 48 22" aria-hidden="true">
        <rect x="1" y="1" width="40" height="20" rx="3" fill="none" stroke="#fff" stroke-width="2"/>
        <rect x="4" y="4" width="9" height="14" fill="#fff"/>
        <rect x="43" y="7" width="4" height="8" rx="1" fill="#fff"/>
      </svg>
    </div>
  </header>

  <h1 class="brand-title">
    <span class="line-main">Brindlewood Hound</span>
    <span class="line-sub">House</span>
  </h1>

  <div class="kennel-illustration" role="img" aria-label="Cartoon dog sitting beside a kennel with a food bowl"></div>

  <svg class="hero-ring" width="532" height="532" viewBox="0 0 532 532" aria-hidden="true">
    <circle cx="266" cy="266" r="234" fill="var(--cream)" stroke="var(--forest)" stroke-width="64"/>
  </svg>
  <div class="hero-photo" role="img" aria-label="Photo of a golden puppy with eyes closed, head tilted up"></div>

  <nav class="carousel-dots" aria-label="Slides">
    <span class="is-active"></span><span></span><span></span><span></span>
  </nav>

  <button class="call-button" type="button">Call Us</button>
</main>
</body>
</html>
```